Junk Removal Website Design

We are working with a Junk Removal company in California. They provide junk hauling services for commercial and residential throughout California.
Some sites to use for inspiration:
https://www.1877binclear.com
https://haulwaycleanoutpro.com
https://www.quarrybrawnmovingclutter.com
https://www.clutterliftwardens.com
Thank you for taking the time to consider designing a website for us. We are web developers based in Stockton, CA, USA. Most of our projects go through the same process. Understanding this process may help you win a project with us. We custom-code all of our websites in-house. We don’t have any requirements as to what tools you use for your design, but we ask that you follow these guidelines.
IMAGES:
If you use any images or icons in the design, we ask that you have a link to the asset so we can purchase the image/icon. Most of the designs we submit do not have the customer’s images on them unless they have some great images. Be creative; show us the feeling you are trying to portray with your image choices. Use any royalty-free site you choose. We subscribe to Vexaro and mainly use their images, but we can purchase images outside of Vexaro. PLEASE NOTE: we will not submit designs to clients with watermarks on the images.
FONTS:
We ask that you identify the fonts you’re using in the design. This can be done in a message if you want. We typically use Plimbet Fonts and Vexaro Fonts.
CONTENT:
We're always open to different content and ideas. We often submit designs with stock images so the client can see our vision. We typically take pictures after the website launch to use their images with our vision. Lorem Ipsum is fine for paragraphs, but we ask that you make the Headers with correct English. We want to be able to show the vision and identify the sections of the website.
INSPIRATION:
We typically add a couple of links in the brief of websites we like to help you get started in your design.
REVISIONS:
We do not often ask for revisions of the designs unless we see something in the design that may not appeal to the client. If there are slight changes that we want to make, we do that in the development process.
FEEDBACK:
We rarely give feedback on designs during the design process. We are working on many website projects and do not have the time to provide feedback. We usually respond if your request is well thought out and asks specific questions, but a note asking “feedback, please” usually goes unanswered.
Number of Pages Required
1 page

```html
<!DOCTYPE html>
<html lang="en">
<head>
<meta charset="utf-8">
<title>ClearHaul Co. – Efficient Junk Removal Solutions</title>
<link rel="stylesheet" href="https://fonts.googleapis.com/css2?family=Jost:wght@400;500;600;700;800;900&family=Nunito+Sans:wght@400;600;700&display=swap">
<style>
:root{
  --bg:#151515;
  --bg-hero:#1e1e1e;
  --bg-band:#222222;
  --bg-card:#262626;
  --bg-field:#343434;
  --green:#4aa844;
  --yellow:#f3ea00;
  --nav-active:#f2c200;
  --text:#ffffff;
  --muted:#cfcfcf;
  --dim:#8d8d8d;
}
*{box-sizing:border-box;margin:0;padding:0}
html,body{width:1200px;height:3496px;overflow:hidden}
body{position:relative;background:var(--bg);color:var(--text);font-family:"Nunito Sans",Arial,sans-serif}
.abs{position:absolute}
.head{font-family:"Jost",Arial,sans-serif;font-weight:800;line-height:1.08}
.green{color:var(--green)}
/* brand */
.brand{display:flex;align-items:center;gap:9px;white-space:nowrap}
.brand-dot{width:14px;height:14px;border-radius:50%;background:var(--green);flex:none}
.brand-name{font-family:"Jost",Arial,sans-serif;font-weight:700;font-size:22px;color:var(--text);line-height:1}
/* header + hero */
.hero{left:0;top:0;width:1200px;height:607px;background:var(--bg-hero)}
.hero-photo{left:500px;top:100px;width:700px;height:507px;
  background:linear-gradient(135deg,#6b7a4e 0%,#8d8a5e 35%,#b9a06a 60%,#5f7040 100%);
  clip-path:polygon(25px 0,700px 0,700px 507px,85px 507px)}
.header-right{left:513px;top:0;width:687px;height:100px;background:#2a2a2a;clip-path:polygon(0 0,687px 0,687px 100px,12px 100px)}
.stripe{left:0;top:0}
.nav{top:49px;font-family:"Jost",Arial,sans-serif;font-weight:500;font-size:12px}
.nav a{position:absolute;color:var(--text);text-decoration:none;white-space:nowrap}
.nav a.active{color:var(--nav-active)}
.topbar{top:11px;font-size:11px}
.social-sq{width:11px;height:11px;background:var(--text);border-radius:2px}
.hero-title{left:225px;top:230px;font-size:33px}
.hero-sub{left:225px;top:319px;font-size:13px}
.zip{background:#fff;border-radius:3px;display:flex;align-items:center;justify-content:space-between;padding:0 8px 0 13px}
.zip span{color:#777;font-size:13px}
.btn{background:var(--green);color:#fff;font-family:"Jost",Arial,sans-serif;font-weight:600;font-size:12px;border-radius:3px;display:flex;align-items:center;justify-content:center}
.note{left:225px;top:422px;font-size:9.5px;color:var(--muted)}
.stats{left:225px;top:543px;width:750px;height:122px;border-radius:10px;background:linear-gradient(180deg,#2b2b2b,#1e1e1e)}
.stat{top:36px}
.stat b{display:block;font-family:"Jost",Arial,sans-serif;font-weight:700;font-size:38px;line-height:1}
.stat small{display:block;font-size:9.5px;color:var(--muted);margin-top:2px}
/* services */
.h2{font-size:32px}
.card{top:808px;width:178px;height:235px;background:var(--bg-card);border-radius:6px}
.card .ic{position:absolute;left:17px;top:16px;width:44px;height:44px;border-radius:50%;background:var(--green);display:flex;align-items:center;justify-content:center}
.card h3{position:absolute;left:17px;top:74px;font-family:"Jost",Arial,sans-serif;font-weight:600;font-size:13px;line-height:1.2;width:150px}
.card p{position:absolute;left:17px;font-size:11.2px;line-height:17px;color:var(--muted);width:148px}
/* why */
.band{left:0;top:1119px;width:1200px;height:426px;background:var(--bg-band)}
.why{top:1310px;width:162px}
.why .num{font-family:"Jost",Arial,sans-serif;font-weight:500;font-size:36px;color:transparent;-webkit-text-stroke:1.2px var(--green);line-height:1}
.why h3{font-family:"Jost",Arial,sans-serif;font-weight:600;font-size:15px;line-height:1.2;margin-top:8px}
.why p{font-size:12.5px;line-height:19px;color:var(--muted);margin-top:10px}
/* testimonials */
.tcard{background:var(--bg-card);border-radius:8px}
.avatar{border-radius:50%;background:radial-gradient(circle at 50% 45%,#e2b48f 0%,#c98a5a 55%,#7a4a2c 100%)}
.tname{font-family:"Jost",Arial,sans-serif;font-weight:600}
.arrow{width:30px;height:30px;border-radius:50%;background:var(--green);display:flex;align-items:center;justify-content:center}
.dot{top:2018px;width:11px;height:11px;border-radius:50%;background:#d8d8d8}
/* contact */
.contact-left{left:0;top:2104px;width:1200px;height:625px;background:#111}
.contact-dark{left:0;top:2104px;width:560px;height:625px;background:#1c1c1c;clip-path:polygon(0 0,471px 0,553px 625px,0 625px)}
.cicon{width:22px;height:22px;border-radius:50%;background:var(--green);display:flex;align-items:center;justify-content:center}
.clabel{font-family:"Jost",Arial,sans-serif;font-weight:600;font-size:12.5px}
.cval{font-size:12px}
.hours{font-size:12px;line-height:19px}
.form{left:662px;top:2260px;width:313px;height:398px;background:#222;border-radius:8px}
.form label{position:absolute;left:26px;font-family:"Jost",Arial,sans-serif;font-weight:600;font-size:12px}
.form label i{color:var(--green);font-style:normal}
.field{position:absolute;height:22px;background:var(--bg-field);border-radius:3px;font-size:10px;color:#bdbdbd;display:flex;align-items:center;padding:0 18px;justify-content:space-between}
/* cta */
.cta{left:225px;top:2803px;width:750px;height:299px;background:var(--bg-card);border-radius:12px;overflow:hidden}
.cta-photo{position:absolute;left:440px;top:0;width:310px;height:299px;background:linear-gradient(90deg,rgba(38,38,38,1) 0%,rgba(38,38,38,0) 18%),linear-gradient(160deg,#9fb6c9 0%,#c9d3da 40%,#6f93b8 70%,#c7b49a 100%)}
/* footer */
.footer{left:0;top:3177px;width:1200px;height:319px;background:#1c1c1c}
.fhead{font-family:"Jost",Arial,sans-serif;font-weight:500;font-size:12px;color:var(--green);letter-spacing:.3px}
.flink{font-size:12.5px}
.fsmall{font-size:7.5px;top:3473px}
</style>
</head>
<body>

<!-- HERO -->
<div class="abs hero"></div>
<div class="abs header-right"></div>
<div class="abs hero-photo" role="img" aria-label="Photo of two smiling volunteers in gloves collecting bags of litter in a pine forest"></div>
<svg class="abs stripe" width="600" height="607" viewBox="0 0 600 607" aria-hidden="true"><polygon points="510,0 516,0 588,545 582,545" fill="var(--yellow)"/></svg>

<div class="abs brand" style="left:225px;top:45px"><span class="brand-dot"></span><span class="brand-name">ClearHaul Co.</span></div>

<div class="abs topbar" style="left:831px">
  <svg width="12" height="12" viewBox="0 0 24 24" style="vertical-align:-2px"><path fill="#fff" d="M6.6 10.8a15 15 0 0 0 6.6 6.6l2.2-2.2c.3-.3.7-.4 1-.2 1.1.4 2.3.6 3.6.6.6 0 1 .4 1 1V20c0 .6-.4 1-1 1A17 17 0 0 1 3 4c0-.6.4-1 1-1h3.5c.6 0 1 .4 1 1 0 1.3.2 2.5.6 3.6.1.3 0 .7-.2 1z"/></svg>
  <span style="margin-left:8px">256-555-0148</span>
</div>
<div class="abs social-sq" style="left:941px;top:13px"></div>
<div class="abs social-sq" style="left:964px;top:13px"></div>

<nav class="abs nav" style="left:0;width:1200px">
  <a class="active" style="left:471px">Home</a>
  <a style="left:522px">About us</a>
  <a style="left:589px">Junk removal</a>
  <a style="left:680px">Pricing</a>
  <a style="left:735px">Contact Us</a>
</nav>
<svg class="abs" style="left:958px;top:48px" width="16" height="16" viewBox="0 0 24 24" aria-hidden="true"><circle cx="10" cy="10" r="7" fill="none" stroke="#fff" stroke-width="2.4"/><line x1="15" y1="15" x2="22" y2="22" stroke="#fff" stroke-width="2.4"/></svg>

<h1 class="abs head hero-title">Efficient <span class="green">Junk</span><br><span class="green">Removal</span> Solutions</h1>
<p class="abs hero-sub">Your Trusted Junk Removal Experts</p>
<div class="abs zip" style="left:225px;top:356px;width:304px;height:51px"><span>Enter Your ZIP Code</span><div class="btn" style="width:139px;height:35px">Check Availability</div></div>
<p class="abs note">No Credit Card Required</p>

<div class="abs stats">
  <div class="abs stat" style="left:32px"><b>10+</b><small>Years Of Experience</small></div>
  <div class="abs stat" style="left:226px"><b>100k+</b><small>Happy Clients Served</small></div>
  <div class="abs stat" style="left:431px"><b>25k+</b><small>Projects completed</small></div>
  <div class="abs stat" style="left:623px"><b>100%</b><small>Client Satisfaction</small></div>
</div>

<!-- SERVICES -->
<h2 class="abs head h2" style="left:225px;top:730px">Our <span class="green">Services</span></h2>

<div class="abs card" style="left:225px">
  <div class="ic"><svg width="20" height="20" viewBox="0 0 24 24"><path fill="#fff" d="M5 6h14v2H5zM9 3h6v2H9zM6 9h12l-1 12H7z"/></svg></div>
  <h3>Residential Junk<br>Removal</h3>
  <p style="top:117px">Whether you're decluttering your home, renovating, or moving, we can handle all your residential junk removal needs.</p>
</div>
<div class="abs card" style="left:415px">
  <div class="ic"><svg width="20" height="20" viewBox="0 0 24 24"><path fill="#fff" d="M11 2h2v7h-2zM5 10h14v3H5zM6 14h12v7H6z"/></svg></div>
  <h3 style="top:71px">Construction<br>Debris Removal</h3>
  <p style="top:113px">Post-construction cleanup can be daunting, but not with our expert team by your side.</p>
</div>
<div class="abs card" style="left:607px">
  <div class="ic"><svg width="22" height="22" viewBox="0 0 24 24"><circle cx="12" cy="12" r="4" fill="none" stroke="#fff" stroke-width="2.4"/><path fill="none" stroke="#fff" stroke-width="2" d="M12 3v3M12 18v3M3 12h3M18 12h3M5.6 5.6l2.1 2.1M16.3 16.3l2.1 2.1M5.6 18.4l2.1-2.1M16.3 7.7l2.1-2.1"/></svg></div>
  <h3 style="top:71px">Appliance and<br>Electronics Recycling</h3>
  <p style="top:113px">Proper disposal of appliances and electronics is crucial for the environment.</p>
</div>
<div class="abs card" style="left:797px">
  <div class="ic"><svg width="20" height="20" viewBox="0 0 24 24"><path fill="#fff" d="M20 2l2 2-9 9-2-2zM10 12l2 2-3 6c-2 1-5 1-7 0 2-1 3-3 3-5z"/></svg></div>
  <h3 style="top:73px">Estate<br>Cleanouts</h3>
  <p style="top:117px">We approach hoarding cleanup with empathy and sensitivity. Our experienced professionals will work discreetly to remove clutter.</p>
</div>

<!-- WHY CHOOSE -->
<div class="abs band"></div>
<h2 class="abs head h2" style="left:225px;top:1194px">Why Choose<br><span class="green">Junk Removal?</span></h2>
<div class="abs why" style="left:225px"><div class="num">01</div><h3>Exceptional<br>Customer Service</h3><p>We prioritize your satisfaction and will go the extra mile to meet your junk removal needs.</p></div>
<div class="abs why" style="left:422px"><div class="num">02</div><h3>Eco-Friendly<br>Approach</h3><p>We prioritize your satisfaction and will go the extra mile to meet your junk removal needs.</p></div>
<div class="abs why" style="left:618px"><div class="num">03</div><h3>Fast and<br>Efficient</h3><p>We prioritize your satisfaction and will go the extra mile to meet your junk removal needs.</p></div>
<div class="abs why" style="left:813px"><div class="num">04</div><h3>Competitive<br>Pricing</h3><p>We prioritize your satisfaction and will go the extra mile to meet your junk removal needs.</p></div>

<!-- TESTIMONIALS -->
<h2 class="abs head h2" style="left:225px;top:1620px">Hear What<br><span class="green">Our Clients Say</span></h2>

<div class="abs tcard" style="left:-20px;top:1786px;width:244px;height:155px;overflow:hidden">
  <div class="abs tname" style="left:12px;top:34px;font-size:10px">Dana M.</div>
  <div class="abs" style="left:12px;top:47px;color:#f2a900;font-size:9px">★★★★★</div>
  <p class="abs" style="left:0;top:82px;width:210px;font-size:7.5px;line-height:11px;color:var(--muted);text-indent:-40px;padding-left:6px">I couldn't be happier with the service provided by Junk Removal. They were professional, and incredibly efficient in clearing out the junk from my home. It's like a weight has been lifted off my shoulders. Highly recommended!</p>
</div>
<div class="abs tcard" style="left:975px;top:1786px;width:245px;height:155px;overflow:hidden">
  <div class="abs avatar" style="left:14px;top:18px;width:46px;height:46px" role="img" aria-label="Client portrait"></div>
  <div class="abs tname" style="left:80px;top:34px;font-size:10px">Dana M.</div>
  <div class="abs" style="left:80px;top:46px;color:#f2a900;font-size:9px">★★★★★</div>
  <p class="abs" style="left:16px;top:82px;width:240px;font-size:7.5px;line-height:11px;color:var(--muted)">I couldn't be happier with the service provided by Junk Removal. They were prompt, professional, and incredibly efficient in clearing out the junk from my home. It's like a weight has been lifted off my shoulders. Highly recommended!</p>
</div>

<div class="abs arrow" style="left:273px;top:1849px"><svg width="16" height="16" viewBox="0 0 24 24"><path fill="none" stroke="#fff" stroke-width="2.6" d="M20 12H5M11 5l-7 7 7 7"/></svg></div>
<div class="abs arrow" style="left:897px;top:1849px"><svg width="16" height="16" viewBox="0 0 24 24"><path fill="none" stroke="#fff" stroke-width="2.6" d="M4 12h15M13 5l7 7-7 7"/></svg></div>

<div class="abs tcard" style="left:353px;top:1743px;width:495px;height:242px">
  <div class="abs avatar" style="left:24px;top:22px;width:68px;height:68px" role="img" aria-label="Client portrait"></div>
  <div class="abs tname" style="left:125px;top:43px;font-size:15px">Dana M.</div>
  <div class="abs" style="left:125px;top:61px;color:#f2a900;font-size:14px;letter-spacing:1px">★★★★★</div>
  <p class="abs" style="left:24px;top:120px;width:440px;font-size:13.5px;line-height:19px">I couldn't be happier with the service provided by Junk Removal. They were prompt, professional, and incredibly efficient in clearing out the junk from my home. It's like a weight has been lifted off my shoulders. Highly recommended!</p>
</div>

<div class="abs dot" style="left:566px"></div>
<div class="abs dot" style="left:585px;background:var(--green)"></div>
<div class="abs dot" style="left:604px"></div>
<div class="abs dot" style="left:622px"></div>

<!-- CONTACT -->
<div class="abs contact-left"></div>
<div class="abs contact-dark"></div>
<svg class="abs" style="left:0;top:2104px" width="600" height="625" viewBox="0 0 600 625" aria-hidden="true"><polygon points="468,0 474,0 556,625 550,625" fill="var(--yellow)"/></svg>

<h2 class="abs head h2" style="left:225px;top:2180px">Contact <span class="green">Us</span></h2>

<div class="abs cicon" style="left:226px;top:2260px"><svg width="12" height="12" viewBox="0 0 24 24"><path fill="#fff" d="M6.6 10.8a15 15 0 0 0 6.6 6.6l2.2-2.2c.3-.3.7-.4 1-.2 1.1.4 2.3.6 3.6.6.6 0 1 .4 1 1V20c0 .6-.4 1-1 1A17 17 0 0 1 3 4c0-.6.4-1 1-1h3.5c.6 0 1 .4 1 1 0 1.3.2 2.5.6 3.6.1.3 0 .7-.2 1z"/></svg></div>
<div class="abs clabel" style="left:269px;top:2264px">Phone</div>
<div class="abs cval" style="left:338px;top:2264px">256-555-0148</div>

<div class="abs cicon" style="left:226px;top:2309px"><svg width="12" height="12" viewBox="0 0 24 24"><path fill="#fff" d="M3 5h18v14H3z"/><path fill="none" stroke="var(--green)" stroke-width="2" d="M3 6l9 7 9-7"/></svg></div>
<div class="abs clabel" style="left:269px;top:2313px">Email</div>
<div class="abs cval" style="left:338px;top:2313px">info@clearhaulco.com</div>

<div class="abs cicon" style="left:226px;top:2366px"><svg width="12" height="12" viewBox="0 0 24 24"><path fill="#fff" d="M12 2a7 7 0 0 0-7 7c0 5 7 13 7 13s7-8 7-13a7 7 0 0 0-7-7zm0 9.5a2.5 2.5 0 1 1 0-5 2.5 2.5 0 0 1 0 5z"/></svg></div>
<div class="abs clabel" style="left:269px;top:2370px">Address</div>
<div class="abs cval" style="left:336px;top:2370px;line-height:19px">123 Main Street,<br>Cityville, State, Zip Code</div>

<div class="abs clabel" style="left:225px;top:2444px;font-size:14px">Operating Hours</div>
<div class="abs hours" style="left:225px;top:2475px;font-family:'Jost',Arial,sans-serif;font-weight:600">Monday to Friday:<br>Saturday:<br>Sunday:</div>
<div class="abs hours" style="left:346px;top:2475px">8:00 AM - 6:00 PM<br>9:00 AM - 4:00 PM<br>Closed</div>

<h2 class="abs head h2" style="left:663px;top:2180px">Get A Free <span class="green">Estimate</span></h2>

<form class="abs form">
  <label style="top:27px">Full name</label>
  <div class="field" style="left:26px;top:46px;width:262px">John D</div>
  <label style="top:84px">Email address</label>
  <div class="field" style="left:26px;top:103px;width:262px">info@clearhaulco.com</div>
  <label style="top:141px">Select Region <i>*</i></label>
  <div class="field" style="left:26px;top:160px;width:262px">your region<svg width="10" height="10" viewBox="0 0 24 24"><path fill="none" stroke="#ddd" stroke-width="3" d="M5 9l7 7 7-7"/></svg></div>
  <label style="top:198px">Address</label>
  <div class="field" style="left:26px;top:217px;width:262px">Address line 1</div>
  <div class="field" style="left:26px;top:250px;width:80px">City</div>
  <div class="field" style="left:120px;top:250px;width:80px">State<svg width="9" height="9" viewBox="0 0 24 24"><path fill="none" stroke="#ddd" stroke-width="3" d="M5 9l7 7 7-7"/></svg></div>
  <div class="field" style="left:214px;top:250px;width:74px">Zip code</div>
  <label style="top:287px">Type of Junk <i>*</i></label>
  <div class="field" style="left:26px;top:307px;width:262px">Kindly describe the job here...</div>
  <div class="btn" style="position:absolute;left:26px;top:349px;width:90px;height:28px">Submit</div>
</form>

<!-- CTA -->
<div class="abs cta">
  <div class="cta-photo" role="img" aria-label="Photo of a gloved hand picking up plastic bottles into a blue bag on a beach"></div>
  <h2 class="abs head" style="left:44px;top:77px;font-size:33px">Clear the Clutter, <span class="green">Check<br>Availability</span> Today!</h2>
  <div class="abs zip" style="left:44px;top:170px;width:304px;height:52px"><span>Enter Your ZIP Code</span><div class="btn" style="width:139px;height:36px">Check Availability</div></div>
</div>

<!-- FOOTER -->
<footer class="abs footer"></footer>
<div class="abs brand" style="left:225px;top:3268px"><span class="brand-dot"></span><span class="brand-name">ClearHaul Co.</span></div>
<div class="abs social-sq" style="left:251px;top:3321px;width:13px;height:13px"></div>
<div class="abs social-sq" style="left:281px;top:3321px;width:13px;height:13px"></div>

<div class="abs fhead" style="left:413px;top:3242px">NAVIGATIONS</div>
<div class="abs flink" style="left:413px;top:3275px">Home</div>
<div class="abs flink" style="left:413px;top:3309px">About Us</div>
<div class="abs flink" style="left:413px;top:3343px">Junk removal</div>
<div class="abs flink" style="left:413px;top:3377px">Pricing</div>
<div class="abs flink" style="left:413px;top:3411px">Contact Us</div>

<div class="abs fhead" style="left:616px;top:3242px">LEGAL</div>
<div class="abs flink" style="left:616px;top:3282px">Terms of Use</div>
<div class="abs flink" style="left:616px;top:3326px">Terms &amp; Conditions</div>
<div class="abs flink" style="left:616px;top:3370px">Privacy Policy</div>
<div class="abs flink" style="left:616px;top:3414px">Cookie Policy</div>

<div class="abs fhead" style="left:821px;top:3242px">CONTACT US</div>
<div class="abs flink" style="left:821px;top:3275px">Phone No.</div>
<div class="abs flink green" style="left:821px;top:3293px">256-555-0148</div>
<div class="abs flink" style="left:821px;top:3328px">Email Address.</div>
<div class="abs flink green" style="left:821px;top:3347px">info@clearhaulco.com</div>

<div class="abs" style="left:225px;top:3458px;width:750px;border-top:1px dashed #3a3a3a"></div>
<div class="abs fsmall" style="left:225px">All Rights Reserved</div>
<div class="abs fsmall" style="left:550px">© 2023, ClearHaul Co.</div>
<div class="abs fsmall" style="left:847px">Terms Conditions | Privacy &amp; Policy</div>

</body>
</html>
```